KR business cards
Business cards for Consulting outfit
Project: KR business cards
KR business cards -
Creative Brief
Professional
No name
No address
info@vosk-lantern.example
vosk-lantern.example
Would like business cards for 8 different people. No address on the card
Logo + We define the standard

```html
<!DOCTYPE html>
<html lang="en">
<head>
<meta charset="utf-8">
<title>KR stationery set – vosk-lantern</title>
<link rel="stylesheet" href="https://fonts.googleapis.com/css2?family=Crimson+Text:wght@400;600&display=swap">
<style>
  :root {
    --backdrop-light: #b4b4b6;
    --backdrop-dark: #6e6f72;
    --paper: #ffffff;
    --brand-red: #c8262b;
    --brand-red-light: #dd3a3e;
    --brand-red-dark: #9e1b20;
    --ink: #5a5a5a;
    --ink-soft: #8a8a8a;
  }
  * { box-sizing: border-box; margin: 0; padding: 0; }
  html, body { width: 1200px; height: 626px; overflow: hidden; }
  body {
    position: relative;
    font-family: "Crimson Text", Georgia, serif;
    background: radial-gradient(ellipse at 50% 45%, var(--backdrop-light) 0%, #98989b 55%, var(--backdrop-dark) 100%);
  }
  .sheet {
    position: absolute;
    background: var(--paper);
    box-shadow: 0 2px 6px rgba(0,0,0,.25);
  }
  .band {
    position: absolute;
    height: 18px;
    background: linear-gradient(180deg, var(--brand-red-light), var(--brand-red) 55%, var(--brand-red-dark));
  }
  .brand {
    position: absolute;
    left: 0; right: 0;
    text-align: center;
    color: var(--ink);
    line-height: 1;
  }
  .brand-mark {
    display: block;
    color: var(--brand-red);
    font-weight: 600;
    letter-spacing: 1px;
  }
  .brand-name { display: block; font-weight: 400; }
  .fine {
    position: absolute;
    left: 0; right: 0;
    text-align: center;
    color: var(--ink-soft);
    font-size: 6px;
    letter-spacing: .3px;
  }

  /* business card front */
  .card-front { left: 34px; top: 197px; width: 180px; height: 91px; }
  .card-front .brand { top: 20px; }
  .card-front .brand-mark { font-size: 16px; }
  .card-front .brand-name { font-size: 13px; margin-top: 2px; }
  .card-front .fine { top: 68px; }

  /* business card back */
  .card-back { left: 34px; top: 305px; width: 180px; height: 93px; }
  .card-back .band { top: 18px; height: 8px; }
  .card-back .band-left { left: 0; width: 54px; }
  .card-back .band-right { right: 0; width: 54px; }
  .card-back .brand { top: 13px; }
  .card-back .brand-mark { font-size: 12px; }
  .card-back .brand-name { font-size: 10px; margin-top: 1px; }
  .card-back .holder {
    position: absolute; left: 0; right: 0; top: 47px;
    text-align: center; color: var(--brand-red); font-size: 8px; line-height: 1.1;
  }
  .card-back .holder-role { color: var(--ink-soft); font-size: 6px; }
  .card-back .fine { top: 72px; line-height: 1.3; color: var(--brand-red); font-size: 5.5px; }

  /* letterhead */
  .letterhead { left: 233px; top: 31px; width: 374px; height: 559px; }
  .letterhead .band { top: 29px; }
  .letterhead .band-left { left: 0; width: 128px; }
  .letterhead .band-right { right: 0; width: 65px; }
  .letterhead .brand { top: 16px; }
  .letterhead .brand-mark { font-size: 20px; }
  .letterhead .brand-name { font-size: 15px; margin-top: 2px; }
  .letterhead .fine { top: 533px; }

  /* envelope back */
  .envelope-back { left: 679px; top: 79px; width: 487px; height: 195px; }
  .envelope-back svg { position: absolute; left: 0; top: 0; }

  /* envelope front */
  .envelope-front { left: 679px; top: 338px; width: 487px; height: 185px; }
  .envelope-front .band { top: 34px; }
  .envelope-front .band-left { left: 0; width: 125px; }
  .envelope-front .band-right { right: 0; width: 130px; }
  .envelope-front .brand { top: 22px; left: -30px; }
  .envelope-front .brand-mark { font-size: 18px; }
  .envelope-front .brand-name { font-size: 14px; margin-top: 2px; }
  .envelope-front .fine { top: 148px; }
</style>
</head>
<body>

  <section class="sheet card-front" aria-label="Business card, front">
    <div class="brand">
      <span class="brand-mark">KR</span>
      <span class="brand-name">vosk-lantern</span>
    </div>
    <p class="fine">We define the standard</p>
  </section>

  <section class="sheet card-back" aria-label="Business card, back">
    <div class="band band-left"></div>
    <div class="band band-right"></div>
    <div class="brand">
      <span class="brand-mark">KR</span>
      <span class="brand-name">vosk-lantern</span>
    </div>
    <div class="holder">
      <span class="holder-name">Ada Norr</span><br>
      <span class="holder-role">Consultant</span>
    </div>
    <p class="fine">info@vosk-lantern.example<br>T 0800 555 0100</p>
  </section>

  <section class="sheet letterhead" aria-label="Letterhead">
    <div class="band band-left"></div>
    <div class="band band-right"></div>
    <div class="brand">
      <span class="brand-mark">KR</span>
      <span class="brand-name">vosk-lantern</span>
    </div>
    <p class="fine">T 0800 555 0100 · info@vosk-lantern.example · vosk-lantern.example</p>
  </section>

  <section class="sheet envelope-back" aria-label="Envelope, back with flap">
    <svg width="487" height="195" viewBox="0 0 487 195">
      <defs>
        <radialGradient id="flap-fill" cx="50%" cy="30%" r="70%">
          <stop offset="0" stop-color="#dd3a3e"/>
          <stop offset="1" stop-color="#a81e23"/>
        </radialGradient>
      </defs>
      <path d="M0 0 H487 V92 Q470 98 440 102 L260 110 Q243 111 226 110 L47 102 Q17 98 0 92 Z" fill="url(#flap-fill)"/>
    </svg>
  </section>

  <section class="sheet envelope-front" aria-label="Envelope, front">
    <div class="band band-left"></div>
    <div class="band band-right"></div>
    <div class="brand">
      <span class="brand-mark">KR</span>
      <span class="brand-name">vosk-lantern</span>
    </div>
    <p class="fine">T 0800 555 0100 · info@vosk-lantern.example · vosk-lantern.example</p>
  </section>

</body>
</html>
```